Lotvantage.com Webpage Design

Design Brief for lotvantage.com (Copy of Brief also in attached Word file)

Name of Website- lotvantage.com (existing logo and look & feel of website to be changed)

Logo - Finalised. The logo files are attached with the brief as “logo.jpeg”. The “Blue- Grey” version of the logo is for use on lighter backgrounds and the “Orange-White” version of the logo is for use on darker backgrounds. (A full Black version of the logo is also attached). Both versions may be used in different parts of the website. All attached files are in .png format.
Status - The website in functional and is undergoing user trials. However, we want to improve the look & feel of the website so at it seems
a. cotemporary,
b. Easy to Navigate
c. professional and
d. Vibrant.

Please visit ‘lotvantage.com’ to check out the website and its functionalities – please use it only as a reference for the features & functions to be provided, however the designer should use a ‘Free Hand’ in designing the composition of various parts of the webpage without getting too influenced by the existing design

Objective of the Website ‘lotvantage.com –
a. It is a portal focussed on listing of ‘Retail’ specific real-estate properties by developers, owners and realty brokers. The properties shall listed under the following four categories-
i. Retail Malls
ii. Shopping Complexes
iii. High-street shops
iv. Retail Warehouses
*refer lotvantage.com for better clarity

b. The abovementioned properties shall be listed either for ‘Sale’ or ‘rent\lease’ or both

c. Users shall visit the site in case they wish to acquire a retail \ shop space either on ‘sale’ or ‘rent’. These Users would be able to specify the ‘Search Criteria’ through the tool-bars provided on the website – the ‘Search Criteria’ shall comprise of ‘Type of space category’, ‘City’, ‘Locality’, transaction type ie ‘Rent \ Sale’ and ‘Area Range’

d. The main revenue model for the website shall be listing fee ( or advertising charges ) payable by those listing their properties on the website.

Three Main Pages of Website (lotvantage.com) that need to be designed -
a. Main Home Page (visit the web link - http://lotvantage.com/ ) - The main home page has the “Search Toolbar” for specifying of Search Criteria by the User. It shall also have the following features & functions-
i. Main Advertising Banner
ii. Featured Projects
iii. New Launches
iv. Toolbar with buttons – ‘Advertise with Us’, ‘Listings Alert’, ‘Lot Mavens’, ‘Advertiser Login’

b. Property Listings Page (visit the web link - http://lotvantage.com/gurgaon-in-india ) - The List of property options that match the Criteria specified by the ‘User’ get displayed on this page.

c. Property Detail Page - When the ‘User’ clicks on the “More….” Button on the ‘Property Listings Page’ (given in point b. above) the web page with the details of the property opens. (For Example – visit the web link - http://lotvantage.com/brevo-Shopping-Complex-brevo-quadrel-gurgaon-636 )

Note:- Please refer to attached ‘Shopping’ related images the designer may use them on the website to provide a look & feel of retail if required – either separately or rotate in a single window

Target Market(s)

Retailers & Investors looking for retail space, Real Estate Brokers, Developers

Industry/Entity Type

Advertising

Number of Pages Required

3 page

Requirements
Must have
• Refer to existing site lotvantage.com -- all the existing functionalities are a must have.
Nice to have
• The Designer may use the retail related images on the website if required for making it more vibrant. Refer attached images Shopping(1-6).jpg

```html
<!DOCTYPE html>
<html lang="en">
<head>
<meta charset="utf-8">
<title>Lotvantage.com – Home</title>
<link href="https://fonts.googleapis.com/css2?family=Open+Sans:wght@400;600;700;800&display=swap" rel="stylesheet">
<style>
:root{
  --ink:#1e1e1e;
  --bar:#1b1b1b;
  --nav:#2b2b2b;
  --nav-active:#474747;
  --text:#3a3a3a;
  --muted:#7a7a7a;
  --line:#e2e2e2;
  --band:#ececec;
  --white:#ffffff;
  --footer:#242424;
  --footer-deep:#161616;
  --footer-text:#b9b9b9;
  --rent:#2f2f2f;
  --sale:#c8342c;
}
*{box-sizing:border-box;margin:0;padding:0}
html,body{width:698px;height:1200px;overflow:hidden;background:var(--white)}
body{font-family:"Open Sans",Arial,sans-serif;color:var(--text);position:relative}
.page{position:relative;width:698px;height:1200px;overflow:hidden}

/* top utility bar */
.utility-bar{position:absolute;top:0;left:0;width:698px;height:20px;background:var(--bar);color:#cfcfcf;font-size:7px}
.utility-bar .social{position:absolute;left:104px;top:6px;display:flex;gap:4px}
.social i{display:block;width:8px;height:8px;background:#6b6b6b;border-radius:1px}
.utility-bar .contact{position:absolute;right:104px;top:5px;display:flex;gap:12px}
.utility-bar .contact span{display:flex;align-items:center;gap:3px}

/* header */
.site-header{position:absolute;top:20px;left:0;width:698px;height:44px;background:var(--white)}
.brand{position:absolute;left:104px;top:13px;display:flex;align-items:center;gap:5px}
.brand .mark{width:16px;height:16px;background:var(--ink)}
.brand .name{font-size:15px;font-weight:800;color:var(--ink);letter-spacing:-.3px}
.main-nav{position:absolute;left:276px;top:0;width:318px;height:44px;background:var(--nav);display:flex;align-items:center}
.main-nav a{color:#eaeaea;text-decoration:none;font-size:6.6px;font-weight:700;text-transform:uppercase;height:44px;display:flex;align-items:center;padding:0 7px}
.main-nav a.active{background:var(--nav-active)}
.main-nav .account{margin-left:auto;display:flex}
.main-nav .account a{font-weight:600;text-transform:none;font-size:7px}

/* hero */
.hero{position:absolute;top:64px;left:0;width:698px;height:262px;background:linear-gradient(180deg,#9fb8cf 0%,#d9dfe3 38%,#e9e4d8 60%,#b7c9b1 78%,#5fa9c9 100%)}
.search-panel{position:absolute;left:116px;top:32px;width:408px;height:180px;background:rgba(255,255,255,.82)}
.search-panel h2{height:17px;background:var(--ink);color:var(--white);font-size:8px;font-weight:700;padding:3px 8px}
.search-tabs{display:flex;margin:6px 8px 0}
.search-tabs span{font-size:7px;padding:3px 8px;background:#dcdcdc;color:var(--text);border:1px solid #c9c9c9;border-bottom:none}
.search-tabs span.on{background:var(--white);font-weight:700}
.search-body{margin:0 8px;background:var(--white);height:128px;padding:8px 8px;border:1px solid #d3d3d3}
.field-row{display:flex;gap:8px;margin-bottom:10px}
.field{flex:1}
.field label{display:block;font-size:6.5px;font-weight:700;color:var(--ink);margin-bottom:3px}
.field .select{height:14px;border:1px solid #cfcfcf;font-size:6px;color:var(--muted);padding:2px 4px;position:relative}
.field .select:after{content:"";position:absolute;right:4px;top:5px;border:3px solid transparent;border-top-color:#777}
.search-btn{position:absolute;right:16px;bottom:14px;background:var(--ink);color:var(--white);font-size:6.5px;font-weight:700;text-transform:uppercase;padding:5px 9px}

/* services */
.services{position:absolute;top:326px;left:104px;width:490px;height:110px;display:flex;gap:14px;padding-top:16px}
.service{flex:1;display:flex;gap:7px}
.service .icon{flex:none;width:34px;height:34px;border-radius:50%;background:var(--ink);display:flex;align-items:center;justify-content:center}
.service h3{font-size:9.5px;font-weight:700;color:var(--ink);margin:2px 0 3px}
.service p{font-size:6px;line-height:1.45;color:var(--muted)}
.service .more{display:block;text-align:right;font-size:6.5px;font-weight:700;color:var(--ink);margin-top:3px}

.band{position:absolute;left:0;width:698px;height:14px;background:var(--band)}

/* section headings */
.section-head{position:absolute;left:104px;width:490px;display:flex;align-items:center;justify-content:space-between}
.section-head h2{font-size:13px;font-weight:700;color:var(--ink)}
.arrows{display:flex;gap:2px}
.arrows i{width:11px;height:11px;background:var(--ink);display:flex;align-items:center;justify-content:center}
.arrows i:first-child{background:#9a9a9a}

/* featured */
.featured-grid{position:absolute;top:488px;left:104px;width:490px;display:flex;gap:12px}
.property-card{width:113.5px;border:1px solid var(--line)}
.property-card .photo{height:62px;position:relative}
.tag{position:absolute;right:0;bottom:0;font-size:6px;font-weight:700;color:var(--white);padding:2px 6px}
.tag.rent{background:var(--rent)}
.tag.sale{background:var(--sale)}
.property-card .info{padding:4px 5px 6px}
.property-card h4{font-size:8px;font-weight:700;color:var(--ink);margin-bottom:3px}
.meta{display:flex;justify-content:space-between;font-size:5.5px;color:var(--muted);line-height:1.5}
.meta b{color:var(--ink);font-size:6.5px}
.read-more{display:block;margin-top:4px;background:var(--ink);color:var(--white);font-size:6px;font-weight:700;text-align:center;padding:3px 0}

/* new launches */
.launch-grid{position:absolute;top:706px;left:104px;width:490px;display:grid;grid-template-columns:repeat(3,1fr);column-gap:12px;row-gap:26px}
.launch-card{display:flex;gap:5px;height:88px}
.launch-card .photo{flex:none;width:72px;height:88px;position:relative}
.launch-card .tag{left:0;right:auto;top:0;bottom:auto}
.launch-card .info{flex:1;display:flex;flex-direction:column;justify-content:space-between;padding:2px 0}
.launch-card h4{font-size:7.5px;font-weight:700;color:var(--ink);line-height:1.2}
.launch-card .price{font-size:7.5px;font-weight:700;color:var(--ink)}
.launch-card .read-more{width:40px;margin-left:auto}

/* photo tones */
.tone-a{background:linear-gradient(160deg,#7fa6d0,#b9c8d6 55%,#7b6a5a)}
.tone-b{background:linear-gradient(160deg,#8fb3d9,#d26c3b 60%,#a04a2a)}
.tone-c{background:linear-gradient(160deg,#a9c3dd,#d8d2c6 55%,#8d8b84)}
.tone-d{background:linear-gradient(160deg,#6d7db0,#b7b9d9 55%,#e3e3ee)}
.tone-e{background:linear-gradient(160deg,#6a2c3a,#c2455f 50%,#e6b7c0)}
.tone-f{background:linear-gradient(160deg,#8a6fb5,#c7b3dd 55%,#efe6f4)}

/* footer */
.site-footer{position:absolute;top:976px;left:0;width:698px;height:224px;background:var(--footer);color:var(--footer-text)}
.footer-cols{position:absolute;left:104px;top:14px;width:490px;display:flex;gap:14px}
.footer-col{flex:1}
.footer-col h5{font-size:8.5px;font-weight:700;color:var(--white);margin-bottom:7px}
.footer-col p,.footer-col li{font-size:6px;line-height:1.6}
.footer-col ul{list-style:none}
.footer-col .btn{display:inline-block;margin-top:8px;background:#0f0f0f;color:var(--white);font-size:6px;font-weight:700;padding:3px 8px}
.footer-social{display:flex;gap:4px;margin-bottom:14px}
.footer-social i{width:12px;height:12px;background:#5c5c5c}
.newsletter{display:flex;margin-top:4px}
.newsletter span{flex:1;height:13px;background:var(--white)}
.newsletter b{width:22px;height:13px;background:#0f0f0f}
.contact-line{display:flex;gap:4px;align-items:flex-start;margin-bottom:5px}
.contact-line svg{flex:none;margin-top:1px}
.copyright{position:absolute;left:0;bottom:0;width:698px;height:18px;background:var(--footer-deep);font-size:6px;text-align:center;padding-top:5px;color:#9a9a9a}
</style>
</head>
<body>
<div class="page">

  <div class="utility-bar">
    <div class="social"><i></i><i></i><i></i><i></i></div>
    <div class="contact">
      <span><svg width="7" height="7" viewBox="0 0 10 10"><path d="M2 1l2 2-1 1.5c.6 1.2 1.3 1.9 2.5 2.5L7 6l2 2-1.3 1.3C4.5 9 1 5.5.7 2.3z" fill="#cfcfcf"/></svg>+1 555 014 2290</span>
      <span><svg width="8" height="6" viewBox="0 0 10 7"><rect x=".5" y=".5" width="9" height="6" fill="none" stroke="#cfcfcf"/><path d="M.5.5l4.5 3.5L9.5.5" fill="none" stroke="#cfcfcf"/></svg>hello@lotvantage.com</span>
    </div>
  </div>

  <header class="site-header">
    <div class="brand"><span class="mark"></span><span class="name">lotvantage</span></div>
    <nav class="main-nav">
      <a class="active" href="#">Home</a>
      <a href="#">About Us</a>
      <a href="#">Property Listing</a>
      <a href="#">Property Details</a>
      <div class="account"><a href="#">Login</a><a href="#">Register</a></div>
    </nav>
  </header>

  <section class="hero" role="img" aria-label="Banner photo of a modern retail building with a pool in front">
    <form class="search-panel">
      <h2>Search Your House</h2>
      <div class="search-tabs"><span class="on">All</span><span>Rent</span><span>Sale</span></div>
      <div class="search-body">
        <div class="field-row">
          <div class="field"><label>Type of space</label><div class="select">Shopping Mall</div></div>
          <div class="field"><label>City</label><div class="select">Gurgaon</div></div>
          <div class="field"><label>Locality</label><div class="select">Sector 44</div></div>
          <div class="field"><label>Keywords</label><div class="select">Any</div></div>
        </div>
        <div class="field-row">
          <div class="field"><label>Transaction Type</label><div class="select">Rent</div></div>
          <div class="field"><label>Area Range (sq ft)</label><div class="select">500 - 1000</div></div>
          <div class="field"><label>Budget</label><div class="select">Any</div></div>
          <div class="field"><label>Status</label><div class="select">Ready</div></div>
        </div>
      </div>
      <span class="search-btn">Search Your Property</span>
    </form>
  </section>

  <section class="services">
    <div class="service">
      <span class="icon"><svg width="16" height="16" viewBox="0 0 16 16"><path d="M2 6h3l6-3v10l-6-3H2z" fill="#fff"/></svg></span>
      <div><h3>Advertise with Us</h3><p>Lorem Ipsum is simply dummy text of the printing and typesetting industry. Lorem Ipsum has been the standard dummy text ever since.</p><span class="more">Read More »</span></div>
    </div>
    <div class="service">
      <span class="icon"><svg width="16" height="16" viewBox="0 0 16 16"><path d="M8 2a4 4 0 0 1 4 4v4l1.5 2h-11L4 10V6a4 4 0 0 1 4-4zM6.5 13h3a1.5 1.5 0 0 1-3 0z" fill="#fff"/></svg></span>
      <div><h3>Listing Alert</h3><p>Lorem Ipsum is simply dummy text of the printing and typesetting industry. Lorem Ipsum has been the standard dummy text ever since.</p><span class="more">Read More »</span></div>
    </div>
    <div class="service">
      <span class="icon"><svg width="16" height="16" viewBox="0 0 16 16"><path d="M3 5h10l-1 9H4z" fill="#fff"/><path d="M6 5a2 2 0 0 1 4 0" stroke="#fff" fill="none" stroke-width="1.4"/></svg></span>
      <div><h3>Lot Mavens</h3><p>Lorem Ipsum is simply dummy text of the printing and typesetting industry. Lorem Ipsum has been the standard dummy text ever since.</p><span class="more">Read More »</span></div>
    </div>
  </section>

  <div class="band" style="top:438px"></div>

  <div class="section-head" style="top:464px">
    <h2>Featured Properties</h2>
    <div class="arrows">
      <i><svg width="5" height="6" viewBox="0 0 5 6"><path d="M4 0L0 3l4 3z" fill="#fff"/></svg></i>
      <i><svg width="5" height="6" viewBox="0 0 5 6"><path d="M1 0l4 3-4 3z" fill="#fff"/></svg></i>
    </div>
  </div>

  <section class="featured-grid">
    <article class="property-card">
      <div class="photo tone-a" role="img" aria-label="Photo of a high street retail building"><span class="tag rent">Rent</span></div>
      <div class="info"><h4>Orin 81 High Street</h4><div class="meta"><span>Sizes(Sq.ft) 60 / 850</span><b>$ 250000</b></div><span class="read-more">Read More</span></div>
    </article>
    <article class="property-card">
      <div class="photo tone-b" role="img" aria-label="Photo of a red-brick shopping complex"><span class="tag sale">Sale</span></div>
      <div class="info"><h4>Orin 81 High Street</h4><div class="meta"><span>Sizes(Sq.ft) 60 / 850</span><b>$ 250000</b></div><span class="read-more">Read More</span></div>
    </article>
    <article class="property-card">
      <div class="photo tone-c" role="img" aria-label="Photo of a suburban retail building"><span class="tag rent">Rent</span></div>
      <div class="info"><h4>Orin 81 High Street</h4><div class="meta"><span>Sizes(Sq.ft) 60 / 850</span><b>$ 250000</b></div><span class="read-more">Read More</span></div>
    </article>
    <article class="property-card">
      <div class="photo tone-d" role="img" aria-label="Photo of a shopping mall interior"><span class="tag sale">Sale</span></div>
      <div class="info"><h4>Orin 81 High Street</h4><div class="meta"><span>Sizes(Sq.ft) 60 / 850</span><b>$ 250000</b></div><span class="read-more">Read More</span></div>
    </article>
  </section>

  <div class="band" style="top:648px"></div>

  <div class="section-head" style="top:682px">
    <h2>New Launches</h2>
    <div class="arrows">
      <i><svg width="5" height="6" viewBox="0 0 5 6"><path d="M4 0L0 3l4 3z" fill="#fff"/></svg></i>
      <i><svg width="5" height="6" viewBox="0 0 5 6"><path d="M1 0l4 3-4 3z" fill="#fff"/></svg></i>
    </div>
  </div>

  <section class="launch-grid">
    <article class="launch-card">
      <div class="photo tone-a" role="img" aria-label="Photo of a high street retail building"><span class="tag rent">Rent</span></div>
      <div class="info"><h4>Orin 81 High Street</h4><div class="meta"><span>Sizes(Sq.ft) 60 / 850<br>For Shopping Complex</span></div><span class="price">$ 250000</span><span class="read-more">Read More</span></div>
    </article>
    <article class="launch-card">
      <div class="photo tone-e" role="img" aria-label="Photo of a retail store interior in red tones"><span class="tag sale">Sale</span></div>
      <div class="info"><h4>Orin 81 High Street</h4><div class="meta"><span>Sizes(Sq.ft) 60 / 850<br>For Shopping Complex</span></div><span class="price">$ 250000</span><span class="read-more">Read More</span></div>
    </article>
    <article class="launch-card">
      <div class="photo tone-f" role="img" aria-label="Photo of a boutique interior in purple tones"><span class="tag rent">Rent</span></div>
      <div class="info"><h4>Orin 81 High Street</h4><div class="meta"><span>Sizes(Sq.ft) 60 / 850<br>For Shopping Complex</span></div><span class="price">$ 250000</span><span class="read-more">Read More</span></div>
    </article>
    <article class="launch-card">
      <div class="photo tone-a" role="img" aria-label="Photo of a high street retail building"><span class="tag rent">Rent</span></div>
      <div class="info"><h4>Orin 81 High Street</h4><div class="meta"><span>Sizes(Sq.ft) 60 / 850<br>For Shopping Complex</span></div><span class="price">$ 250000</span><span class="read-more">Read More</span></div>
    </article>
    <article class="launch-card">
      <div class="photo tone-e" role="img" aria-label="Photo of a retail store interior in red tones"><span class="tag sale">Sale</span></div>
      <div class="info"><h4>Orin 81 High Street</h4><div class="meta"><span>Sizes(Sq.ft) 60 / 850<br>For Shopping Complex</span></div><span class="price">$ 250000</span><span class="read-more">Read More</span></div>
    </article>
    <article class="launch-card">
      <div class="photo tone-f" role="img" aria-label="Photo of a boutique interior in purple tones"><span class="tag rent">Rent</span></div>
      <div class="info"><h4>Orin 81 High Street</h4><div class="meta"><span>Sizes(Sq.ft) 60 / 850<br>For Shopping Complex</span></div><span class="price">$ 250000</span><span class="read-more">Read More</span></div>
    </article>
  </section>

  <footer class="site-footer">
    <div class="footer-cols">
      <div class="footer-col">
        <h5>Latest News</h5>
        <p>January 06, 2014</p>
        <p>Lotvantage.com is a specialised web based platform for retail spaces featuring properties across the city.</p>
        <span class="btn">Read More</span>
      </div>
      <div class="footer-col">
        <h5>Follow Us On</h5>
        <div class="footer-social"><i></i><i></i><i></i><i></i></div>
        <h5>Newsletter Signup</h5>
        <div class="newsletter"><span></span><b></b></div>
      </div>
      <div class="footer-col">
        <h5>Quick Links</h5>
        <ul><li>Home</li><li>About Us</li><li>Property Listing</li><li>Property Details</li><li>Advertise With Us</li><li>Contact Us</li></ul>
      </div>
      <div class="footer-col">
        <h5>Contact Us</h5>
        <div class="contact-line"><svg width="7" height="9" viewBox="0 0 7 9"><path d="M3.5 0A3.5 3.5 0 0 0 0 3.5C0 6 3.5 9 3.5 9S7 6 7 3.5A3.5 3.5 0 0 0 3.5 0z" fill="#b9b9b9"/></svg><p>Lorem ipsum is simply<br>dummy text of the print</p></div>
        <div class="contact-line"><svg width="7" height="7" viewBox="0 0 10 10"><path d="M2 1l2 2-1 1.5c.6 1.2 1.3 1.9 2.5 2.5L7 6l2 2-1.3 1.3C4.5 9 1 5.5.7 2.3z" fill="#b9b9b9"/></svg><p>+1 555 014 2290</p></div>
        <div class="contact-line"><svg width="7" height="7" viewBox="0 0 10 10"><circle cx="5" cy="5" r="4.3" fill="none" stroke="#b9b9b9"/><path d="M.7 5h8.6M5 .7c-2 2.5-2 6.1 0 8.6M5 .7c2 2.5 2 6.1 0 8.6" fill="none" stroke="#b9b9b9" stroke-width=".7"/></svg><p>www.lotvantage.com</p></div>
      </div>
    </div>
    <div class="copyright">All Rights Reserved 2014 www.lotvantage.com</div>
  </footer>

</div>
</body>
</html>
```